Brell Harbor Company Business Cards

Front and Back Business Card - logo and text setup - cool design. I need workable photoshop or illustrator files so I can setup each employee card with design that is created
Updates

Hi everyone, thank you for the great entries. Please no more white and blue cards - there are so many already - black and silver only now please. thanks!

Target Market(s)

Construction Industry - Facility Managers

Industry/Entity Type

Construction

Contact Information for Business Card

I really like contemporary simplistic looks - clean neat....not opposed to seeing some black backrounds

Requirements
Must have
• Logo/website address with design on front only - www.brellharbor-example.com (logo attached)
• Back:
• Name/Title/Company Address/Phone/email address
Nice to have
• Cool design
Should not have
• Nothing gimmicky like Fire or Water - since we are a Fire Protection company - it has all been done

```html
<!DOCTYPE html>
<html lang="en">
<head>
<meta charset="utf-8">
<title>Brell Harbor Company – Business Cards</title>
<link rel="stylesheet" href="https://fonts.googleapis.com/css2?family=Nunito+Sans:wght@400;600;800&display=swap">
<style>
  :root {
    --stage: #e9e8e6;
    --black: #151617;
    --black-tint: #2e3032;
    --silver-light: #eceef0;
    --silver: #c9cdd2;
    --silver-mid: #9aa0a7;
    --silver-dark: #6d737a;
    --ink: #1a1b1d;
    --ink-soft: #3c3f43;
    --white: #ffffff;
    --shadow: rgba(0, 0, 0, 0.25);
  }
  * { box-sizing: border-box; margin: 0; padding: 0; }
  html, body { width: 1200px; height: 920px; overflow: hidden; }
  body {
    background: var(--stage);
    font-family: "Nunito Sans", Arial, sans-serif;
    position: relative;
  }
  .card {
    position: absolute;
    top: 312px;
    width: 536px;
    height: 300px;
    box-shadow: 0 6px 18px var(--shadow);
  }
  /* Front */
  .card--front {
    left: 46px;
    background: var(--black);
  }
  .front-name {
    position: absolute;
    left: 0; right: 0;
    top: 110px;
    text-align: center;
    font-weight: 800;
    font-size: 50px;
    letter-spacing: -0.5px;
    color: var(--black-tint);
  }
  .front-web {
    position: absolute;
    left: 0; right: 0;
    bottom: 26px;
    text-align: center;
    font-size: 14px;
    letter-spacing: 1px;
    color: var(--silver-mid);
  }
  .front-web .web-domain { color: var(--silver); }
  /* Back */
  .card--back {
    left: 629px;
    background: linear-gradient(135deg, var(--silver-light) 0%, var(--silver) 100%);
  }
  .brand {
    position: absolute;
    left: 38px;
    top: 48px;
    display: flex;
    align-items: center;
    gap: 10px;
  }
  .brand-mark {
    width: 14px; height: 14px;
    background: var(--silver-dark);
  }
  .brand-name {
    font-weight: 800;
    font-size: 40px;
    letter-spacing: -0.5px;
    color: var(--ink);
    line-height: 1;
  }
  .name-bar {
    position: absolute;
    left: 0;
    top: 142px;
    width: 7px;
    height: 38px;
    background: var(--black);
  }
  .person-name {
    position: absolute;
    left: 38px;
    top: 138px;
    font-weight: 800;
    font-size: 19px;
    letter-spacing: 0.5px;
    color: var(--ink);
  }
  .person-title {
    position: absolute;
    left: 38px;
    top: 166px;
    font-size: 12px;
    color: var(--ink-soft);
  }
  .contacts {
    position: absolute;
    left: 38px;
    top: 207px;
    list-style: none;
  }
  .contacts li {
    display: flex;
    align-items: center;
    gap: 8px;
    height: 21.5px;
    font-size: 13px;
    color: var(--ink-soft);
    letter-spacing: 0.3px;
  }
  .contacts svg { width: 14px; height: 14px; flex: none; }
  .address {
    position: absolute;
    right: 36px;
    top: 228px;
    text-align: right;
    font-size: 13px;
    line-height: 21.5px;
    color: var(--ink-soft);
    letter-spacing: 0.3px;
  }
</style>
</head>
<body>
  <section class="card card--front" aria-label="Card front">
    <div class="front-name">Brell Harbor</div>
    <div class="front-web">www.<span class="web-domain">brellharbor-example</span>.com</div>
  </section>

  <section class="card card--back" aria-label="Card back">
    <div class="brand">
      <span class="brand-mark"></span>
      <span class="brand-name">Brell Harbor</span>
    </div>
    <span class="name-bar"></span>
    <div class="person-name">DANA WHITLOCK</div>
    <div class="person-title">Director</div>
    <ul class="contacts">
      <li>
        <svg viewBox="0 0 14 14" aria-hidden="true"><circle cx="7" cy="7" r="6.3" fill="none" stroke="#6d737a" stroke-width="1.2"/><path d="M4.6 3.8l1.3-.3.7 1.7-.8.6c.4.9 1 1.5 1.9 1.9l.6-.8 1.7.7-.3 1.3c-2.7.2-5.3-2.4-5.1-5.1z" fill="#151617"/></svg>
        (555) 014-2270
      </li>
      <li>
        <svg viewBox="0 0 14 14" aria-hidden="true"><circle cx="7" cy="7" r="6.3" fill="none" stroke="#6d737a" stroke-width="1.2"/><rect x="3.6" y="4.6" width="6.8" height="4.8" fill="none" stroke="#151617" stroke-width="1"/><path d="M3.6 4.8L7 7.4l3.4-2.6" fill="none" stroke="#151617" stroke-width="1"/></svg>
        info@brellharbor-example.com
      </li>
      <li>
        <svg viewBox="0 0 14 14" aria-hidden="true"><circle cx="7" cy="7" r="6.3" fill="none" stroke="#6d737a" stroke-width="1.2"/><circle cx="7" cy="7" r="3.2" fill="none" stroke="#151617" stroke-width="1"/><path d="M3.8 7h6.4M7 3.8v6.4" stroke="#151617" stroke-width="0.8"/></svg>
        www.brellharbor-example.com
      </li>
    </ul>
    <div class="address">48 Quarry Lane<br>Marden Point, NY 10990</div>
  </section>
</body>
</html>
```